Cloud Phone Service Brochure

We need a brochure for a Cloud Phone Service offering that we offer in Canada. We're a small company that cares about our client's success and protects their privacy. We would like to see designs that reflect us as a stable, trustworthy company which is also fast moving and leading edge. We see ourselves more like Quenby than Harn. Mosaic Vault has built our logo and business card, and we look forward to moving ahead here. I've attached our Business Card file so you have our logo as well as my own shot at some thoughts about content written as a trifold. That specific content does not need to be used, nor does it need to be a trifold. Those phone pictures are the actual phones we use.

```html
<!DOCTYPE html>
<html lang="en">
<head>
<meta charset="utf-8">
<title>Cloud Phone Service Brochure – Pages 3 and 4</title>
<link rel="stylesheet" href="https://fonts.googleapis.com/css2?family=Open+Sans:wdth,wght@75..100,300..600&family=Tinos&display=swap">
<style>
  :root {
    --page-bg: #ffffff;
    --navy: #1d3c78;
    --navy-deep: #16306a;
    --navy-light: #2a4f93;
    --title-blue: #2f9ad8;
    --feature-text: #c3c9e6;
    --sky: #8eaad8;
    --spec-text: #17213a;
    --white: #ffffff;
    --caption: #111111;
  }
  * { box-sizing: border-box; margin: 0; padding: 0; }
  html, body {
    width: 1200px; height: 776px; overflow: hidden;
    background: var(--page-bg);
  }
  .canvas { position: relative; width: 1200px; height: 776px; }

  .spread {
    position: absolute; left: 124px; top: 72px;
    width: 921px; height: 590px;
  }

  /* Page 3 */
  .page-features {
    position: absolute; left: 0; top: 0; width: 462px; height: 590px;
    background:
      linear-gradient(160deg, rgba(120,160,230,0.18) 0%, rgba(0,0,0,0) 35%),
      linear-gradient(170deg, rgba(0,0,0,0) 30%, rgba(200,90,170,0.16) 45%, rgba(0,0,0,0) 58%),
      linear-gradient(180deg, var(--navy-light) 0%, var(--navy) 45%, var(--navy-deep) 100%);
    font-family: "Open Sans", sans-serif;
    font-stretch: 75%;
    font-weight: 300;
  }
  .features-title {
    position: absolute; left: 47px; top: 34px; width: 330px;
    color: var(--title-blue); font-weight: 300;
    font-size: 54px; line-height: 44px;
  }
  .features-title span { display: block; }
  .features-title .title-second { text-align: right; }
  .feature-list {
    position: absolute; left: 51px; top: 158px;
    list-style: none; color: var(--feature-text);
    font-size: 23px; line-height: 27.9px;
  }

  /* Page 4 */
  .page-video {
    position: absolute; left: 462px; top: 0; width: 459px; height: 590px;
    background: var(--sky); overflow: hidden;
    font-family: "Open Sans", sans-serif; font-stretch: 75%;
  }
  .meeting-photo {
    position: absolute; left: 0; top: 215px; width: 459px; height: 375px;
    background: linear-gradient(180deg, var(--sky) 0%, #a9b9cf 20%, #6d7f96 55%, #3a4452 100%);
  }
  .vertical-heading {
    position: absolute; color: var(--white);
    font-size: 28px; font-weight: 300; line-height: 28px;
    white-space: nowrap; transform: rotate(-90deg); transform-origin: 0 0;
  }
  .heading-video { left: 2px; top: 320px; }
  .heading-room { left: 27px; top: 256px; }
  .spec-list {
    position: absolute; left: 89px; top: 119px;
    list-style: none; color: var(--spec-text);
    font-size: 10.5px; line-height: 13.8px; white-space: nowrap;
  }
  .spec-list .sep { padding: 0 4px; }

  .page-caption {
    position: absolute; left: 124px; top: 678px;
    font-family: "Tinos", serif; font-size: 12px; color: var(--caption);
  }
</style>
</head>
<body>
<div class="canvas">
  <div class="spread">
    <section class="page-features">
      <h1 class="features-title">
        <span class="title-first">Phone Service</span>
        <span class="title-second">Features</span>
      </h1>
      <ul class="feature-list">
        <li>All features and functions are included</li>
        <li>Conference line included</li>
        <li>Toll free number included</li>
        <li>North America LD included</li>
        <li>Monthly billing with no contract</li>
        <li>No hardware or installation costs</li>
        <li>Any high-speed internet service</li>
        <li>Retain your existing phone number</li>
        <li>Voicemail to email</li>
        <li>Find me &amp; Follow me</li>
        <li>Call recording</li>
      </ul>
    </section>

    <section class="page-video">
      <div class="meeting-photo" role="img" aria-label="Photo of a business team meeting around a conference table in a glass-walled office"></div>
      <h2 class="vertical-heading heading-video">Video Conferencing</h2>
      <h2 class="vertical-heading heading-room">Room Configuration</h2>
      <ul class="spec-list">
        <li>120 Simultaneous video streams<span class="sep">|</span>Most conference sources supported</li>
        <li>Video Conf Room System<span class="sep">|</span>Video Phones<span class="sep">|</span>PC &amp; Orchard Computers<span class="sep">|</span>Droidal &amp; PomOS Devices</li>
        <li>SIP PBXes<span class="sep">|</span>PSTN Phones<span class="sep">|</span>Connect Vidora &amp; Circlet Live<span class="sep">|</span>1080p HD at 30 fps</li>
        <li>Multi-location conferencing<span class="sep">|</span>Meeting Controls<span class="sep">|</span>Screen Sharing</li>
        <li>Customizable Registration options<span class="sep">|</span>Email Follow-up options<span class="sep">|</span>10 simultaneous sessions</li>
        <li>Encrypted connections</li>
      </ul>
    </section>
  </div>
  <p class="page-caption">Pages 3 and 4</p>
</div>
</body>
</html>
```